Artwork for New Single, ”Keep Still”

Unique design describing Silence.
Use the pictures provided for ideas.
Looking for something out the box, different.
Make this stand out. Modern times or futuristic.
Imagination welcomed.
BRISTLECONE MEDIA INC.
Artist name is Bristlecone
Song Title: Keep Still

Target Market(s)

Millennials, Trap music listeners, Hardcore rap fans.

Colors

Designer to choose colors to be used in the design.

Requirements
Nice to have
• Bold, serious designs. Make a statement. Masculine, professional in nature.

```html
<!DOCTYPE html>
<html lang="en">
<head>
<meta charset="utf-8">
<title>Keep Still — Bristlecone</title>
<link rel="stylesheet" href="https://fonts.googleapis.com/css2?family=Cinzel:wght@400;600&display=swap">
<style>
  :root {
    --paper: #ffffff;
    --ring-light: #f1f1f1;
    --ring-mid: #dcdcdc;
    --ring-edge: #c6c6c6;
    --note-tone: #9c9c9c;
    --title-ink: #383838;
    --artist-ink: #cbcbcb;
  }
  html, body {
    margin: 0;
    padding: 0;
    width: 1200px;
    height: 1200px;
    overflow: hidden;
    background: var(--paper);
  }
  .cover {
    position: relative;
    width: 1200px;
    height: 1200px;
    background: var(--paper);
  }
  .emblem {
    position: absolute;
    left: 0;
    top: 0;
    width: 1200px;
    height: 1200px;
  }
  .song-title,
  .artist-name {
    position: absolute;
    left: 0;
    right: 0;
    margin: 0;
    text-align: center;
    font-family: "Cinzel", "Trajan Pro", serif;
    white-space: nowrap;
  }
  .song-title {
    top: 982px;
    font-size: 76px;
    line-height: 76px;
    font-weight: 600;
    color: var(--title-ink);
  }
  .artist-name {
    top: 1056px;
    font-size: 78px;
    line-height: 78px;
    font-weight: 400;
    color: var(--artist-ink);
  }
</style>
</head>
<body>
  <main class="cover">
    <svg class="emblem" viewBox="0 0 1200 1200" xmlns="http://www.w3.org/2000/svg">
      <defs>
        <radialGradient id="ring-shade" cx="603" cy="506" r="416" gradientUnits="userSpaceOnUse">
          <stop offset="0.79" stop-color="var(--ring-mid)"/>
          <stop offset="0.895" stop-color="var(--ring-light)"/>
          <stop offset="1" stop-color="var(--ring-mid)"/>
        </radialGradient>
      </defs>
      <path class="ornament-ring" role="img"
            aria-label="Ring of interlocking outlined squares forming a lace-like border around the centre"
            fill="url(#ring-shade)" fill-rule="evenodd"
            stroke="var(--ring-edge)" stroke-width="2"
            d="M603 90 a416 416 0 1 0 0.01 0 Z M603 176 a330 330 0 1 1 -0.01 0 Z"/>
      <rect class="note-figure" role="img"
            aria-label="Grey musical note with a stem and three flags"
            x="542" y="345" width="122" height="323" rx="40"
            fill="var(--note-tone)"/>
    </svg>
    <h1 class="song-title">Keep Still</h1>
    <p class="artist-name">Bristlecone</p>
  </main>
</body>
</html>
```